Toronto's Airline, based in Downtown looking for a whole new look and feel.

SoarVex is looking for a new look in our website. We are an airline based at Marlow Quay Airfield in Toronto. You can view our current website/services at www.soarvex-example.com. We are expanding our services and look forward to a very sleek and modernized website. Please view the different pages on our website, we also need to add several new plane types as we have expanded and the website is not current. Would also be interesting to have a news feed or update feed through a widget which would be easy to use and update. we will also be implementing 2 third party programs called bookplume and skyledgra on the website, both are tour based and airline based sales and management functions.

Target Market(s)

Commuters, travel, tourism, dates, general public

Industry/Entity Type

Airline

Coding

Coded - Design and coding required

Number of Pages Required

5+ page

Font styles to use
Other font styles liked:
• Toronto subway font would be nice

Requirements
Must have
• A modern feel, easy to use, our booking function is currently a bit confusing which we will be working on. Content can be taken from our current website www.soarvex-example.com
Nice to have
• work with out theme colours of blue and light grey

```html
<!DOCTYPE html>
<html lang="en">
<head>
<meta charset="utf-8">
<title>SoarVex — Toronto's Airline</title>
<link rel="stylesheet" href="https://fonts.googleapis.com/css2?family=Roboto:wght@400;500;700&family=Roboto+Condensed:wght@400;700&display=swap">
<style>
:root{
  --blue:#2c5ea8;
  --blue-dark:#28508f;
  --blue-btn:#345f9f;
  --accent:#3a8ee6;
  --ink:#333;
  --muted:#666;
  --grey-bg:#efefef;
  --grey-line:#d6d6d6;
  --white:#fff;
}
*{box-sizing:border-box;margin:0;padding:0}
html,body{width:1200px;height:3020px;overflow:hidden}
body{position:relative;background:var(--white);font-family:"Roboto",Arial,sans-serif;color:var(--ink)}
.abs{position:absolute}
h1,h2,h3{font-family:"Roboto Condensed","Arial Narrow",sans-serif;font-weight:400}

/* header */
.site-header{position:absolute;left:0;top:0;width:1200px;height:88px;background:var(--white)}
.brand{position:absolute;left:104px;top:22px;display:flex;align-items:center;gap:12px}
.brand-dot{width:40px;height:40px;border-radius:50%;background:var(--blue)}
.brand-name{font-family:"Roboto Condensed",sans-serif;font-weight:700;font-size:30px;color:var(--blue);letter-spacing:1px}
.main-nav{position:absolute;right:124px;top:36px;display:flex;gap:30px;font-family:"Roboto Condensed",sans-serif;font-size:14px;color:#666}
.main-nav .active{color:var(--blue)}

/* hero */
.hero{position:absolute;left:0;top:88px;width:1200px;height:596px;
  background:radial-gradient(ellipse at 50% 90%,#5a4d3a 0%,rgba(40,40,60,0) 45%),linear-gradient(180deg,#1b2a4c 0%,#152038 45%,#2b2c38 100%)}
.hero-arrow{position:absolute;top:314px}
.tabs{position:absolute;left:244px;top:236px;display:flex;gap:4px}
.tab{height:46px;padding:0 26px;line-height:46px;font-family:"Roboto Condensed",sans-serif;font-size:17px;color:var(--white);background:var(--blue-btn)}
.tab.current{background:#f1f1f1;color:#333}
.tour-card{position:absolute;left:244px;top:282px;width:710px;height:226px;background:#f1f1f1}
.tour-photo{position:absolute;left:30px;top:30px;width:228px;height:168px;background:linear-gradient(160deg,#8aa0b8,#4c6074 60%,#6b7a6a)}
.tour-title{position:absolute;left:280px;top:26px;width:400px;font-size:28px;line-height:36px;color:#222;text-transform:uppercase}
.tour-text{position:absolute;left:280px;top:106px;width:400px;font-size:11.5px;line-height:20px;color:#777}
.pager{position:absolute;right:14px;top:12px;font-size:14px;color:var(--blue)}
.btn{display:inline-flex;align-items:center;gap:8px;background:var(--blue-btn);color:var(--white);font-family:"Roboto Condensed",sans-serif;font-size:12px;text-transform:uppercase}
.tour-card .btn{position:absolute;left:576px;top:178px;height:34px;padding:0 12px}

/* about */
.about{position:absolute;left:0;top:684px;width:600px;height:457px;background:var(--white)}
.section-title{font-size:33px;color:var(--blue);text-transform:uppercase}
.about .section-title{position:absolute;left:100px;top:80px}
.about-lead{position:absolute;left:100px;top:134px;width:460px;font-size:18px;line-height:26px;font-weight:500;color:var(--blue)}
.about-text{position:absolute;left:100px;top:200px;width:460px;font-size:13px;line-height:21px;color:#666}
.about .btn{position:absolute;left:100px;top:312px;height:34px;padding:0 14px}
.video{position:absolute;left:600px;top:684px;width:600px;height:457px;background:#000}
.video-title{position:absolute;left:30px;top:20px;font-size:12px;color:#eee}
.video-brand{position:absolute;left:0;width:600px;top:186px;text-align:center;font-family:"Roboto Condensed",sans-serif;font-weight:700;font-size:56px;color:#3a3f48;letter-spacing:4px}
.video-bar{position:absolute;left:40px;top:418px;width:520px;height:3px;background:#d32222}
.video-time{position:absolute;left:90px;top:428px;font-size:10px;color:#ccc}

/* news */
.news-intro{position:absolute;left:0;top:1141px;width:1200px;height:214px;background:var(--grey-bg)}
.news-intro .section-title{position:absolute;left:98px;top:48px}
.news-intro p{position:absolute;left:98px;top:104px;width:1000px;font-size:11.5px;line-height:24px;color:#666}
.news-grid{position:absolute;left:0;top:1355px;width:1200px;height:593px;display:grid;grid-template-columns:598px 598px;grid-template-rows:295px 295px;gap:3px 4px;background:#ccc}
.news-tile{position:relative}
.news-meta{position:absolute;left:74px;top:176px;font-size:14px;color:var(--white)}
.news-meta .date{color:var(--accent)}
.news-meta .sep{margin:0 8px;color:#ddd}
.news-head{position:absolute;left:74px;top:200px;font-size:17px;color:var(--white)}
.news-tile:nth-child(2) .news-meta,.news-tile:nth-child(2) .news-head,
.news-tile:nth-child(4) .news-meta,.news-tile:nth-child(4) .news-head{left:34px}
.view-all{position:absolute;left:0;top:1948px;width:1200px;height:90px;background:linear-gradient(180deg,#f3f3f3,#d9d9d9);text-align:center;line-height:90px;font-family:"Roboto Condensed",sans-serif;font-size:20px;color:var(--blue);text-transform:uppercase}

/* packages */
.packages{position:absolute;left:0;top:2038px;width:1200px;height:438px;background:var(--white)}
.packages .section-title{position:absolute;left:0;width:1200px;top:30px;text-align:center}
.pkg{position:absolute;top:98px;width:246px;height:290px}
.pkg-photo{height:146px}
.pkg h3{margin:26px 0 0 26px;font-size:23px;color:var(--blue);text-transform:uppercase}
.pkg p{margin:12px 0 0 24px;width:200px;font-size:11.5px;line-height:18px;color:#444}
.pkg.featured{box-shadow:0 2px 8px rgba(0,0,0,.18)}
.notch{position:absolute;left:50px;top:138px;width:0;height:0;border-left:9px solid transparent;border-right:9px solid transparent;border-bottom:9px solid var(--white)}
.pkg-tag{position:absolute;left:102px;top:22px;height:22px;padding:0 8px;line-height:22px;background:var(--blue-btn);color:#fff;font-size:10px;font-family:"Roboto Condensed",sans-serif}
.pkg-icon{position:absolute;top:56px;width:30px;height:30px;display:flex;align-items:center;justify-content:center}

/* contact */
.contact{position:absolute;left:0;top:2476px;width:1200px;height:492px;background:var(--grey-bg)}
.contact .section-title{position:absolute;left:100px;top:48px;font-size:29px}
.contact-lead{position:absolute;left:100px;top:100px;width:300px;font-size:11.5px;line-height:22px;color:#555}
.contact-label{position:absolute;left:100px;font-size:10px;font-weight:700;color:#333;text-transform:uppercase}
.contact-addr{position:absolute;left:100px;top:208px;font-size:10.5px;line-height:20px;color:#555}
.contact-list{position:absolute;left:100px;top:314px;font-size:10.5px;line-height:21px;color:#555;list-style:none}
.contact-list li{display:flex;align-items:center;gap:10px}
.partner{position:absolute;top:420px;font-size:21px;color:var(--blue-dark)}
.field-label{position:absolute;font-size:10px;color:#333}
.field{position:absolute;height:38px;background:var(--white);border:1px solid var(--grey-line)}
.contact .btn{position:absolute;left:444px;top:380px;height:42px;width:162px;padding-left:18px;gap:14px;font-size:11px}

/* footer */
.site-footer{position:absolute;left:0;top:2968px;width:1200px;height:52px;background:var(--grey-bg);border-top:4px solid var(--blue-btn)}
.copyright{position:absolute;left:104px;top:15px;font-size:10px;color:#555}
.foot-nav{position:absolute;right:132px;top:15px;display:flex;gap:28px;font-family:"Roboto Condensed",sans-serif;font-size:12px;color:#333}
</style>
</head>
<body>

<header class="site-header">
  <div class="brand"><span class="brand-dot"></span><span class="brand-name">SOARVEX</span></div>
  <nav class="main-nav">
    <span class="active">HOME</span><span>FLIGHTS</span><span>CHARTER &amp; FLEET</span><span>PACKAGES</span><span>GALLERY</span><span>CONTACT</span><span>FAQ</span>
  </nav>
</header>

<section class="hero" role="img" aria-label="Night view of a lit suspension bridge over the river with a city skyline">
  <svg class="hero-arrow" style="left:104px" width="24" height="36" viewBox="0 0 24 36"><path d="M18 4 6 18l12 14" fill="none" stroke="#fff" stroke-width="4"/></svg>
  <svg class="hero-arrow" style="left:1072px" width="24" height="36" viewBox="0 0 24 36"><path d="M6 4l12 14L6 32" fill="none" stroke="#fff" stroke-width="4"/></svg>
  <div class="tabs">
    <span class="tab current">TOURS</span><span class="tab">FLIGHTS</span><span class="tab">SALES AND MANAGEMENT</span>
  </div>
  <article class="tour-card">
    <span class="pager">&lsaquo;&nbsp;&nbsp;&rsaquo;</span>
    <div class="tour-photo" role="img" aria-label="Aerial view of downtown Toronto with the CN Tower and stadium"></div>
    <h2 class="tour-title">Toronto Aerial Tour &amp; CN Tower Flyby</h2>
    <p class="tour-text">See the vast expanse of Toronto and take in the unique landscape of the Scarborough Bluffs and Toronto Harbourfront. Experience a bird's eye view of the Harbour Dome and downtown Toronto. Then back for 3 passes so close to the CN Tower.</p>
    <span class="btn">Book now
      <svg width="11" height="11" viewBox="0 0 11 11"><path d="M4 1H1v9h9V7M6 1h4v4M10 1 5 6" fill="none" stroke="#fff" stroke-width="1.3"/></svg></span>
  </article>
</section>

<section class="about">
  <h2 class="section-title">About Us</h2>
  <p class="about-lead">Ut enim ad minima veniam, quis nostrum exercitationem ullam corporis suscipit laboriosam,</p>
  <p class="about-text">Lorem ipsum dolor sit amet, consectetur adipiscing elit, sed do eiusmod tempor incididunt ut labore et dolore magna aliqua. Ut enim ad minim veniam, quis nostrud exercitation ullamco laboris nisi ut aliquip ex ea commodo consequat. Duis aute irure dolor in reprehenderit in voluptate velit esse cillum dolore</p>
  <span class="btn">Read more
    <svg width="11" height="11" viewBox="0 0 11 11"><path d="M4 1H1v9h9V7M6 1h4v4M10 1 5 6" fill="none" stroke="#fff" stroke-width="1.3"/></svg></span>
</section>

<section class="video" role="img" aria-label="Video player: SoarVex Toronto-Niagara Shuttle">
  <span class="video-title">SoarVex Toronto-Niagara Shuttle</span>
  <div class="video-brand">SOARVEX</div>
  <svg class="abs" style="left:268px;top:196px" width="64" height="64" viewBox="0 0 64 64"><circle cx="32" cy="32" r="32" fill="#7d7d7d" fill-opacity=".85"/><path d="M25 19v26l21-13z" fill="#fff"/></svg>
  <div class="video-bar"></div>
  <svg class="abs" style="left:44px;top:428px" width="40" height="12" viewBox="0 0 40 12"><path d="M0 1v10l8-5z" fill="#fff"/><path d="M22 4h3l4-3v10l-4-3h-3z" fill="#fff"/></svg>
  <span class="video-time">0:59 / 1:00</span>
</section>

<section class="news-intro">
  <h2 class="section-title">News &amp; Articles</h2>
  <p>Sed ut perspiciatis unde omnis iste natus error sit voluptatem accusantium doloremque laudantium, totam rem aperiam, eaque ipsa quae ab illo inventore veritatis et quasi architecto beatae vitae dicta sunt explicabo. Nemo enim ipsam voluptatem quia voluptas sit aspernatur aut odit aut fugit.</p>
</section>

<section class="news-grid">
  <article class="news-tile" role="img" aria-label="Old European town with a church spire and stone bridge at dusk" style="background:linear-gradient(180deg,#3a4a6a 0%,#6a5a58 50%,#2a2a30 100%)">
    <div class="news-meta"><span class="date">April 12, 2016</span><span class="sep">/</span>Maren Holt<span class="sep">/</span>16 Comments</div>
    <div class="news-head">Lorem ipsum dolor sit amet, consectetur adipiscing</div>
  </article>
  <article class="news-tile" role="img" aria-label="City skyline across the water under a cloudy sky" style="background:linear-gradient(180deg,#4a5f7a 0%,#3a4c64 55%,#1e2c40 100%)">
    <div class="news-meta"><span class="date">April 16, 2016</span><span class="sep">/</span>Maren Holt<span class="sep">/</span>16 Comments</div>
    <div class="news-head">Lorem ipsum dolor sit amet, consectetur adipiscing</div>
  </article>
  <article class="news-tile" role="img" aria-label="Tall downtown towers against a blue sky" style="background:linear-gradient(180deg,#2a4a78 0%,#1d3256 55%,#4a4a4a 100%)">
    <div class="news-meta"><span class="date">Jan 07, 2017</span><span class="sep">/</span>Maren Holt<span class="sep">/</span>16 Comments</div>
    <div class="news-head">Lorem ipsum dolor sit amet, consectetur adipiscing</div>
  </article>
  <article class="news-tile" role="img" aria-label="Night aerial view of the city with the tower lit up" style="background:linear-gradient(180deg,#2a3448 0%,#1a2030 55%,#141824 100%)">
    <div class="news-meta"><span class="date">Jan 05, 2017</span><span class="sep">/</span>Maren Holt<span class="sep">/</span>16 Comments</div>
    <div class="news-head">Lorem ipsum dolor sit amet, consectetur adipiscing</div>
  </article>
</section>

<div class="view-all">View all articles &amp; news</div>

<section class="packages">
  <h2 class="section-title">Packages</h2>
  <article class="pkg" style="left:100px">
    <div class="pkg-photo" role="img" aria-label="Elephants on the savanna at sunset" style="background:linear-gradient(180deg,#d89a4a,#b0763a 60%,#6a4a28)"></div>
    <span class="notch"></span>
    <h3>African Safari</h3>
    <p>Lorem ipsum dolor sit amet, consectetur adipiscing elit, sed do eiusmod tempor incididunt ut [...]</p>
  </article>
  <article class="pkg" style="left:350px">
    <div class="pkg-photo" role="img" aria-label="Desert canyon at sunrise" style="background:linear-gradient(180deg,#e8a040,#a84a38 55%,#5a3a38)"></div>
    <span class="notch"></span>
    <h3>Jewis Heritage</h3>
    <p>Lorem ipsum dolor sit amet, consectetur adipiscing elit, sed do eiusmod tempor incididunt ut [...]</p>
  </article>
  <article class="pkg featured" style="left:602px">
    <div class="pkg-photo" role="img" aria-label="Aerial view of downtown Toronto" style="background:linear-gradient(180deg,#6a7a88,#4c5a64 60%,#3a4640)"></div>
    <span class="pkg-tag">READ MORE</span>
    <span class="pkg-icon" style="left:90px;background:#fff"><svg width="14" height="14" viewBox="0 0 14 14"><circle cx="6" cy="6" r="4" fill="none" stroke="#333" stroke-width="1.8"/><path d="M9 9l4 4" stroke="#333" stroke-width="2"/></svg></span>
    <span class="pkg-icon" style="left:124px;background:var(--blue-btn)"><svg width="12" height="14" viewBox="0 0 12 14"><rect x="1" y="1" width="10" height="12" fill="none" stroke="#fff" stroke-width="1.5"/><path d="M3 5h6M3 8h6M3 11h4" stroke="#fff" stroke-width="1.2"/></svg></span>
    <span class="notch"></span>
    <h3>Toronto</h3>
    <p>Lorem ipsum dolor sit amet, consectetur adipiscing elit, sed do eiusmod tempor incididunt ut [...]</p>
  </article>
  <article class="pkg" style="left:852px">
    <div class="pkg-photo" role="img" aria-label="Lakeside old town with a church spire at dusk" style="background:linear-gradient(180deg,#6a6aa8,#9a6a8a 50%,#3a4a6a)"></div>
    <span class="notch"></span>
    <h3>Switzerland</h3>
    <p>Lorem ipsum dolor sit amet, consectetur adipiscing elit, sed do eiusmod tempor incididunt ut [...]</p>
  </article>
</section>

<section class="contact">
  <h2 class="section-title">Contact Us</h2>
  <p class="contact-lead">Let us help make a lasting impression on you. Tell us about your project and let's begin!</p>
  <span class="contact-label" style="top:188px">Headquarters</span>
  <p class="contact-addr">48 Lakeshore Row<br>Suite 210<br>Toronto, ON M5J 0A1</p>
  <span class="contact-label" style="top:292px">Get in touch</span>
  <ul class="contact-list">
    <li><svg width="11" height="11" viewBox="0 0 11 11"><path d="M2 0h2l1 3-1.5 1a6 6 0 0 0 3 3L8 5.5l3 1v2L9.5 11C5 10.5.5 6 0 1.5z" fill="#333"/></svg>416-555-0142</li>
    <li><svg width="11" height="11" viewBox="0 0 11 11"><circle cx="5.5" cy="5.5" r="5" fill="#333"/></svg>soarvex.desk</li>
    <li><svg width="11" height="11" viewBox="0 0 11 11"><rect x=".5" y="2" width="10" height="7" fill="none" stroke="#333"/><path d="M.5 2l5 4 5-4" fill="none" stroke="#333"/></svg>hello@soarvex-example.com</li>
  </ul>
  <span class="partner" style="left:96px">SKYLEDGRA</span>
  <span class="partner" style="left:270px">bookplume</span>

  <span class="field-label" style="left:444px;top:52px">Full Name</span>
  <div class="field" style="left:444px;top:70px;width:316px"></div>
  <span class="field-label" style="left:784px;top:52px">Email</span>
  <div class="field" style="left:784px;top:70px;width:316px"></div>
  <span class="field-label" style="left:444px;top:136px">Location</span>
  <div class="field" style="left:444px;top:154px;width:316px">
    <svg class="abs" style="right:12px;top:14px" width="12" height="8" viewBox="0 0 12 8"><path d="M1 1l5 5 5-5" fill="none" stroke="#555" stroke-width="1.5"/></svg>
  </div>
  <span class="field-label" style="left:784px;top:136px">Services you're inquiring about</span>
  <div class="field" style="left:784px;top:154px;width:316px">
    <svg class="abs" style="right:14px;top:12px" width="10" height="12" viewBox="0 0 10 12"><rect x=".5" y=".5" width="9" height="11" fill="none" stroke="#777"/><path d="M3 4l2 2 2-2" fill="none" stroke="#777"/></svg>
  </div>
  <span class="field-label" style="left:444px;top:220px">Message</span>
  <div class="field" style="left:444px;top:238px;width:656px;height:124px"></div>
  <span class="btn"><svg width="14" height="12" viewBox="0 0 14 12"><path d="M1 1h12v7H6l-3 3V8H1z" fill="none" stroke="#fff" stroke-width="1.3"/></svg>Send message</span>
</section>

<footer class="site-footer">
  <span class="copyright">&copy; COPYRIGHT 2017 - WWW.SOARVEX-EXAMPLE.COM</span>
  <nav class="foot-nav"><span>HOME</span><span>FLIGHTS</span><span>CHARTER &amp; FLEET</span><span>PACKAGES</span><span>GALLERY</span><span>CONTACT</span><span>FAQ</span></nav>
</footer>

</body>
</html>
```